Animal care facility (Pet Grooming, Doggie daycare, Boarding, Pet Boutique)

Hi there! i came across your wonderful work and would love to work with you! I have a clear image in my head that i want for my bussiness card and stationary. I will go ahead and attach pictures of business cards that i have found to give you an idea of what i would like to see.

My color scheme is a gray back ground and white lettering. So for the card i would like it to be a gray and the logo on the front to be white and done like picture #1. I would like the quality of the card to be a thicker more durable look. I would want just my logo and then underneath my name ( Marisa Thornbury and my title Owner similar to picture #1. I also have somone i am working with so his would need to be (Colin Pratt, General Manager)

Also there is certain information that does need to be on the back of the card so I don't know if a white back with gray lettering would help it be easily read or not.

Alderwick Pet Haven & Spa LLC
862 E. Millrace Rd.
507.264.1193 -Phone
507.268.4410-Fax
Info@alderwickpethavenandspa.com-Email

Grooming- Boarding-Daycare-Pet Boutique

$10.00 OFF First Time Grooming Visit

The font for all of this is using (oranienbaum)
next to the phone fax, email I would like the actual small pictures that I have in one of the photos
Updates

Industry/Entity Type

Pet Care

Requirements
Must have
• Please follow the design of picture 7 I would like to change the direction of the card all together now. I would like the image to be up top and the name and title to be laid out the same and also in the same font as the attached picture. Again I would like all of this on the front to be engraved In white foil on gray matte backing and if we could lighten the color of this card up I would appreciate it but be on the darker side.
• On the back side keep the version you made and flip all the information to be laid out vertically just like the front.

```html
<!DOCTYPE html>
<html lang="en">
<head>
<meta charset="utf-8">
<title>Alderwick Pet Haven &amp; Spa — Stationery</title>
<link rel="stylesheet" href="https://fonts.googleapis.com/css2?family=Oranienbaum&display=swap">
<style>
  :root{
    --backdrop:#262626;
    --heading:#c9c9c9;
    --paper:#e7e7e7;
    --paper-soft:#ececec;
    --ink:#3c3c3c;
    --ink-soft:#5a5a5a;
    --ink-faint:#d4d4d4;
    --band:#4a4a4a;
    --flap:#474747;
    --window:#9c9c9c;
    --window-edge:#6a6a6a;
  }
  *{margin:0;padding:0;box-sizing:border-box}
  html,body{width:1200px;height:801px;overflow:hidden;background:var(--backdrop)}
  body{position:relative;font-family:"Oranienbaum",serif;color:var(--ink)}
  .section-title{position:absolute;color:var(--heading);font-size:31px;font-weight:400;white-space:nowrap;transform:translateX(-50%);letter-spacing:.2px}
  .sheet{position:absolute;background:var(--paper)}
  .edge-band{position:absolute;background:var(--band)}

  .brand-name{position:absolute;display:flex;align-items:center;gap:8px;color:var(--ink);font-weight:400;white-space:nowrap;line-height:1}
  .brand-name .dot{flex:none;border:1.5px solid currentColor;border-radius:50%}
  .brand-name.stacked{flex-direction:column;gap:10px;text-align:center}
  .brand-name.faint{color:var(--ink-faint)}

  .web{position:absolute;font-size:8.5px;letter-spacing:.3px;color:var(--ink)}
  .envelope-window{position:absolute;left:296px;top:98px;width:204px;height:98px;background:var(--window);border:1px solid var(--window-edge);border-radius:7px}
  .flap{position:absolute;left:0;top:0}
  .sender{position:absolute;left:20px;top:176px;font-size:6.8px;line-height:11.6px;color:var(--ink-soft)}
  .sender li{list-style:none;display:flex;align-items:center;gap:6px}
  .sender li:first-child{margin-bottom:2px}
  .sender svg{width:6px;height:6px;fill:var(--ink-soft)}
  .holder{position:absolute;left:0;width:100%;text-align:center;font-size:10.5px;letter-spacing:.6px;line-height:19px}
  .back-info{position:absolute;left:0;width:100%;text-align:center;font-size:7px;color:var(--ink)}
  .contact-row{position:absolute;left:30px;width:98px;text-align:center;font-size:7px}
  .contact-row .icon-line{display:flex;align-items:center;gap:4px;height:8px}
  .contact-row .icon-line span{flex:1;height:1px;background:var(--ink)}
  .contact-row svg{width:7px;height:7px;fill:var(--ink)}
  .contact-row p{margin-top:2px}
</style>
</head>
<body>

<h2 class="section-title" style="left:307px;top:41px">White Compliment / Thank you – Card</h2>
<h2 class="section-title" style="left:890px;top:41px">White Envelope Front &amp; Back Side</h2>
<h2 class="section-title" style="left:306px;top:400px">Business card Front &amp; Back Side</h2>

<!-- Compliment card -->
<section class="sheet compliment-card" style="left:32px;top:106px;width:565px;height:210px">
  <div class="edge-band" style="left:0;top:24px;width:8px;height:104px"></div>
  <div class="brand-name" style="left:20px;top:64px;font-size:12px">
    <i class="dot" style="width:26px;height:26px"></i>Alderwick Pet Haven &amp; Spa
  </div>
  <div class="brand-name faint" style="left:318px;top:92px;font-size:13px">
    <i class="dot" style="width:28px;height:28px"></i>Alderwick Pet Haven &amp; Spa
  </div>
  <p class="web" style="left:308px;top:190px">ALDERWICKPETHAVENANDSPA.COM</p>
</section>

<!-- Envelope front -->
<section class="sheet envelope-front" style="left:637px;top:106px;width:544px;height:269px">
  <div class="edge-band" style="left:0;top:26px;width:9px;height:105px"></div>
  <div class="brand-name" style="left:22px;top:64px;font-size:13px">
    <i class="dot" style="width:28px;height:28px"></i>Alderwick Pet Haven &amp; Spa
  </div>
  <div class="envelope-window"></div>
</section>

<!-- Envelope back -->
<section class="sheet envelope-back" style="left:629px;top:441px;width:557px;height:269px;background:var(--paper-soft)">
  <svg class="flap" width="557" height="110" viewBox="0 0 557 110" aria-hidden="true">
    <path d="M0 0 H541 L538 22 Q536 30 526 33 L282 100 Q268 104 254 100 L10 33 Q2 30 1 20 Z" fill="var(--flap)"/>
  </svg>
  <ul class="sender">
    <li>Alderwick Pet Haven &amp; Spa LLC</li>
    <li><svg viewBox="0 0 10 10"><path d="M5 0a3.5 3.5 0 0 0-3.5 3.5C1.5 6 5 10 5 10s3.5-4 3.5-6.5A3.5 3.5 0 0 0 5 0zm0 5a1.5 1.5 0 1 1 0-3 1.5 1.5 0 0 1 0 3z"/></svg>862 E. Millrace Rd.</li>
    <li><svg viewBox="0 0 10 10"><path d="M2 0l2 2.5-1.2 1.3a6 6 0 0 0 3.4 3.4L7.5 6 10 8l-1.5 2C4 10 0 6 0 1.5z"/></svg>507.264.1193</li>
    <li><svg viewBox="0 0 10 10"><path d="M2.5 0h5v3h-5zM0 3.5h10V8H8v2H2V8H0zM3 6.5V9h4V6.5z"/></svg>507.268.4410</li>
    <li><svg viewBox="0 0 10 10"><path d="M0 1.5h10v7H0zm1 1L5 5.5l4-3z"/></svg>Info@alderwickpethavenandspa.com</li>
  </ul>
</section>

<!-- Business card front -->
<section class="sheet card-front" style="left:122px;top:472px;width:159px;height:288px">
  <div class="brand-name stacked" style="left:0;top:58px;width:159px;font-size:12.5px">
    <i class="dot" style="width:58px;height:58px;border-width:2px"></i>Alderwick Pet Haven &amp; Spa
  </div>
  <div class="holder" style="top:224px">MARISA THORNBURY<br>OWNER</div>
</section>

<!-- Business card back -->
<section class="sheet card-back" style="left:332px;top:470px;width:158px;height:292px">
  <div class="brand-name stacked" style="left:0;top:32px;width:158px;font-size:11px">
    <i class="dot" style="width:40px;height:40px"></i>Alderwick Pet Haven &amp; Spa
  </div>
  <p class="back-info" style="top:135px">Grooming | Boarding | Daycare | Pet Boutique</p>
  <p class="back-info" style="top:148px">$10.00 OFF FIRST TIME GROOMING VISIT</p>

  <div class="contact-row" style="top:184px">
    <div class="icon-line"><span></span><svg viewBox="0 0 10 10"><path d="M2 0l2 2.5-1.2 1.3a6 6 0 0 0 3.4 3.4L7.5 6 10 8l-1.5 2C4 10 0 6 0 1.5z"/></svg><span></span></div>
    <p>507.264.1193</p>
  </div>
  <div class="contact-row" style="top:207px">
    <div class="icon-line"><span></span><svg viewBox="0 0 10 10"><path d="M2.5 0h5v3h-5zM0 3.5h10V8H8v2H2V8H0zM3 6.5V9h4V6.5z"/></svg><span></span></div>
    <p>507.268.4410</p>
  </div>
  <div class="contact-row" style="top:231px">
    <div class="icon-line"><span></span><svg viewBox="0 0 10 10"><path d="M5 0a3.5 3.5 0 0 0-3.5 3.5C1.5 6 5 10 5 10s3.5-4 3.5-6.5A3.5 3.5 0 0 0 5 0zm0 5a1.5 1.5 0 1 1 0-3 1.5 1.5 0 0 1 0 3z"/></svg><span></span></div>
    <p>862 E. Millrace Rd.</p>
  </div>
  <div class="contact-row" style="top:254px;left:14px;width:130px">
    <div class="icon-line" style="margin:0 16px"><span></span><svg viewBox="0 0 10 10"><path d="M0 1.5h10v7H0zm1 1L5 5.5l4-3z"/></svg><span></span></div>
    <p>Info@alderwickpethavenandspa.com</p>
  </div>
</section>

</body>
</html>
```